Serene Spiritual Website Wanted for World Wide Organisation

We need a serene, clean web design for our organisation that works around the world.

What We Do
We aim to bring life into synergy across the world. We inspire, motivate, synchronise, and harmonise. We work with energy which is essential to all of life (environmental, human & animal). Our website must depict the spiritual element of being innately natural and reflect animism.

We have included a PDF attachment with details of the structure, navigation, and some websites for ideas/reference. The logo is also attached.
Updates

Target Market(s)

Anyone over 18yrs looking for answers to life's big questions or looking to develop themselves

Industry/Entity Type

Spiritual/wellbeing/Self Development

Number of Pages Required

5+ page

Requirements
Must have
• It must be serene and natural looking, it must incorporate the logo.
Nice to have
• We have included a Powerpoint document which may help you understand what we need, it is just an idea for structure and style, it is not set in stone so feel free to be as creative as you like!
Should not have
• Not clinical.

```html
<!DOCTYPE html>
<html lang="en">
<head>
<meta charset="utf-8">
<title>Lumen Path — Events</title>
<link rel="stylesheet" href="https://fonts.googleapis.com/css2?family=Montserrat:wght@400;500;600;700&family=Lato:wght@400&display=swap">
<style>
:root{
  --indigo:#3e4069;
  --muted:#7b7ca0;
  --gray:#6a6a6a;
  --gold:#dccb86;
  --gold-line:#e6d8a6;
  --white:#ffffff;
  --card-border:#9a9aa8;
}
*{margin:0;padding:0;box-sizing:border-box}
html,body{width:749px;height:1200px;overflow:hidden;background:var(--white)}
body{position:relative;font-family:'Montserrat',sans-serif;color:var(--indigo)}
.site-header{position:absolute;left:0;top:0;width:749px;height:54px;background:var(--indigo)}
.brand{position:absolute;left:10px;top:19px;display:flex;align-items:center;gap:5px;color:var(--white);font-size:10px;font-weight:600}
.brand-dot{width:12px;height:12px;border-radius:50%;background:var(--gold)}
.main-nav a{position:absolute;top:20px;color:var(--white);font-size:9px;text-decoration:none;font-weight:500}
.hero{position:absolute;left:0;top:54px;width:749px;height:367px;background:linear-gradient(90deg,#cfcebd 0%,#d6d3c6 40%,#e3ddf0 100%)}
.hero-photo{position:absolute;left:0;top:0;width:345px;height:367px;background:radial-gradient(ellipse at 40% 55%,#d9cfa8 0%,#cfc9b0 45%,rgba(207,206,189,0) 75%)}
.hero-quote{position:absolute;left:374px;top:206px;width:330px;font-size:18.5px;line-height:23px;font-weight:600}
.hero-cite{position:absolute;left:374px;top:286px;font-family:'Lato',sans-serif;font-size:7.5px}
.events-title{position:absolute;left:0;top:450px;width:749px;text-align:center;font-size:19px;font-weight:700}
.events-intro{position:absolute;left:110px;top:485px;width:530px;text-align:center;font-size:14px;line-height:17.5px;color:var(--muted)}
.event-card{position:absolute;top:544px;width:181px;height:294px;border:1px solid var(--card-border);border-radius:7px;overflow:hidden;text-align:center;color:var(--gray)}
.event-photo{height:191px;background:linear-gradient(160deg,#8d7a62 0%,#b99d88 45%,#6b4a3e 75%,#e8dcc8 100%)}
.event-title{margin-top:10px;font-size:12.5px;line-height:15px}
.event-sub{margin-top:3px;font-size:9.5px}
.event-date{margin-top:5px;font-size:8.5px}
.event-rule{margin:9px auto 0;width:128px;height:1px;background:var(--gold-line)}
.event-actions{position:absolute;left:26px;top:264px;display:flex;gap:10px}
.btn{height:25px;border-radius:7px;font-size:8.5px;line-height:25px;font-family:'Montserrat',sans-serif}
.btn-outline{width:86px;border:1px solid var(--gold-line);color:var(--gold)}
.btn-fill{width:31px;background:var(--gold);color:var(--white)}
.site-footer{position:absolute;left:3px;top:1029px;width:746px;height:171px;background:var(--indigo);color:var(--white)}
.footer-brand{position:absolute;left:83px;top:58px;display:flex;align-items:center;gap:5px;font-size:10px;font-weight:600}
.footer-nav a{position:absolute;left:216px;color:var(--white);text-decoration:none;font-size:9px;font-weight:500}
.social{position:absolute;width:20px;height:20px;border-radius:50%;background:var(--white);top:52px}
.contact{position:absolute;left:450px;width:280px;text-align:center;font-size:9px;font-weight:500}
.legal{position:absolute;left:0;top:159px;width:980px;text-align:center;font-size:6.5px;font-weight:500}
</style>
</head>
<body>
<header class="site-header">
  <div class="brand"><span class="brand-dot"></span>Lumen Path</div>
  <nav class="main-nav">
    <a style="left:442px">Events</a>
    <a style="left:494px">About</a>
    <a style="left:548px">Synergise</a>
    <a style="left:613px">Wisdom</a>
    <a style="left:672px">Shop</a>
  </nav>
</header>

<section class="hero">
  <div class="hero-photo" role="img" aria-label="Hands holding a brass singing bowl with a wooden striker"></div>
  <p class="hero-quote">Believe in your infinite potential. Your only limitations are those you set upon yourself</p>
  <p class="hero-cite">Mara Ellison, Quiet Rivers</p>
</section>

<h2 class="events-title">Our Events</h2>
<p class="events-intro">Lorem ipsum dolor sit amet, consectetur adipiscing elit, sed do eiusmod tempor incididunt ut labore et dolore magna aliqua. Ut enim ad minim</p>

<article class="event-card" style="left:55px">
  <div class="event-photo" role="img" aria-label="Person meditating cross-legged on a mat beside candles"></div>
  <h3 class="event-title">"Lorem ipsum dolor</h3>
  <p class="event-sub">"Lorem ipsum dolor</p>
  <p class="event-date">22 sept 2022</p>
  <div class="event-rule"></div>
  <div class="event-actions"><span class="btn btn-outline">Learn More</span><span class="btn btn-fill">Save</span></div>
</article>
<article class="event-card" style="left:284px">
  <div class="event-photo" role="img" aria-label="Person meditating cross-legged on a mat beside candles"></div>
  <h3 class="event-title">"Lorem ipsum dolor</h3>
  <p class="event-sub">"Lorem ipsum dolor</p>
  <p class="event-date">22 sept 2022</p>
  <div class="event-rule"></div>
  <div class="event-actions"><span class="btn btn-outline">Learn More</span><span class="btn btn-fill">Save</span></div>
</article>
<article class="event-card" style="left:513px">
  <div class="event-photo" role="img" aria-label="Person meditating cross-legged on a mat beside candles"></div>
  <h3 class="event-title">"Lorem ipsum dolor</h3>
  <p class="event-sub">"Lorem ipsum dolor</p>
  <p class="event-date">22 sept 2022</p>
  <div class="event-rule"></div>
  <div class="event-actions"><span class="btn btn-outline">Learn More</span><span class="btn btn-fill">Save</span></div>
</article>

<footer class="site-footer">
  <div class="footer-brand"><span class="brand-dot"></span>Lumen Path</div>
  <nav class="footer-nav">
    <a style="top:53px">Events</a>
    <a style="top:74px">About</a>
    <a style="top:95px">Synergise</a>
    <a style="top:117px">Wisdom</a>
    <a style="top:138px">Shop</a>
  </nav>
  <span class="social" style="left:500px"></span>
  <span class="social" style="left:553px"></span>
  <span class="social" style="left:606px"></span>
  <span class="social" style="left:659px"></span>
  <p class="contact" style="top:94px">Phone: 555-014-2290</p>
  <p class="contact" style="top:115px">Email: contact@lumenpath.org</p>
  <p class="legal">Terms and Conditions | Privacy Policy&nbsp; Copyright © 2018 Lumen Path Collective, All rights reserved.</p>
</footer>
</body>
</html>
```